Fresh, modern, fun business card for pediatric dental practice

Need a business card for fresh, modern, fun pediatric dental practice

Clean look that matches our website's font and colors

We prefer the look of curved corners on business cards

Target Market(s)

parents (mothers) of young children, professionals, mid-high class

Industry/Entity Type

Dental

Contact Information for Business Card

Maplebrook Pediatric Dentistry
482 Orchard Vale Road
Suite 517
Lititz, PA 17543
555.419.3067
www.maplebrookkidsdental.example

Mara Tevlin, DMD
Colette Varnum, DMD
(we are working on our email address, but we would like that on the card as well)

Font styles to use
Sans Serif

Requirements
Must have
• All info; we would also like to make cards for individual staff members
• colors from our website and color palatte, attatched
• use same font and design as website for branding
Nice to have
• clean, simple card that has a pop of color
• we would like to see a few designs with our tag line "where smiles get brighter"
• we are not sure if we want to have it on there or not
• we would like to see a few designs incorporating the ribbon graphic on our website where the word WELCOME is

```html
<!DOCTYPE html>
<html lang="en">
<head>
<meta charset="utf-8">
<title>Maplebrook Pediatric Dentistry – Business Card</title>
<link rel="stylesheet" href="https://fonts.googleapis.com/css2?family=Montserrat:wght@400;500;600;700&display=swap">
<style>
  :root {
    --page-bg: #e4e4e4;
    --plum: #5b2a57;
    --plum-deep: #4e2149;
    --sun: #f6b925;
    --white: #ffffff;
    --ink: #3f1b3b;
    --radius: 24px;
  }
  * { box-sizing: border-box; margin: 0; padding: 0; }
  html, body { width: 1200px; height: 750px; overflow: hidden; }
  body {
    background: var(--page-bg);
    font-family: "Montserrat", sans-serif;
    position: relative;
  }
  .card {
    position: absolute;
    top: 232px;
    width: 500px;
    height: 286px;
    border-radius: var(--radius);
    overflow: hidden;
  }

  /* Front */
  .card-front {
    left: 70px;
    background: var(--plum);
    display: flex;
    flex-direction: column;
    align-items: center;
    justify-content: center;
    text-align: center;
  }
  .brand-mark {
    width: 34px; height: 34px;
    border-radius: 50%;
    background: var(--sun);
    margin-bottom: 14px;
  }
  .brand-name {
    color: var(--sun);
    font-weight: 600;
    font-size: 25px;
    line-height: 1.2;
    letter-spacing: 0.5px;
    text-transform: lowercase;
  }
  .tagline {
    margin-top: 8px;
    color: var(--sun);
    font-weight: 500;
    font-size: 15px;
    letter-spacing: 0.3px;
  }

  /* Back */
  .card-back {
    left: 630px;
    background: var(--sun);
  }
  .name-panel {
    position: absolute;
    left: 18px; top: 38px;
    width: 230px; height: 212px;
  }
  .name-panel svg { position: absolute; inset: 0; }
  .doctors {
    position: absolute;
    inset: 0;
    display: flex;
    flex-direction: column;
    align-items: center;
    justify-content: center;
    color: var(--white);
    text-align: center;
  }
  .doctor {
    font-weight: 700;
    font-size: 18px;
    line-height: 1.15;
  }
  .doctor .credential { font-weight: 400; font-size: 14px; }
  .doctor-divider {
    width: 140px; height: 2px;
    background: var(--sun);
    margin: 14px 0;
  }
  .contact {
    position: absolute;
    right: 20px; top: 28px; bottom: 28px;
    width: 220px;
    display: flex;
    flex-direction: column;
    justify-content: space-between;
    text-align: right;
    color: var(--ink);
    font-size: 11px;
    line-height: 1.45;
  }
  .contact address { font-style: normal; }
  .contact-rule {
    display: flex;
    align-items: center;
    gap: 10px;
  }
  .contact-rule .rule { flex: 1; height: 1.5px; background: var(--ink); }
  .contact-rule .dot {
    width: 26px; height: 26px;
    border-radius: 50%;
    background: var(--plum);
  }
  .website { font-weight: 600; font-size: 10.5px; white-space: nowrap; }
</style>
</head>
<body>

<section class="card card-front" aria-label="Business card front">
  <div class="brand-mark"></div>
  <p class="brand-name">maplebrook pediatric dentistry</p>
  <p class="tagline">where smiles get brighter</p>
</section>

<section class="card card-back" aria-label="Business card back">
  <div class="name-panel">
    <svg viewBox="0 0 230 212" width="230" height="212" role="img" aria-label="Hand-drawn plum scribble shape behind the dentists' names">
      <polygon points="58,4 172,4 228,106 172,208 58,208 2,106" fill="var(--plum)"/>
    </svg>
    <div class="doctors">
      <p class="doctor">Colette<br>Varnum, <span class="credential">DMD</span></p>
      <div class="doctor-divider"></div>
      <p class="doctor">Mara<br>Tevlin, <span class="credential">DMD</span></p>
    </div>
  </div>

  <div class="contact">
    <address>
      482 Orchard Vale Road<br>
      Suite 517<br>
      Lititz, PA 17543
    </address>
    <div class="contact-rule">
      <span class="rule"></span><span class="dot"></span><span class="rule"></span>
    </div>
    <div>
      <p>555.419.3067</p>
      <p>emailaddress@domain.example</p>
      <p class="website">www.maplebrookkidsdental.example</p>
    </div>
  </div>
</section>

</body>
</html>
```